Commercial painting contractor in need of graphic designs for new trade show booth.

Brindle Holdings, Inc. is a leading commercial and multifamily painter in Texas for new construction interested in growing its repaint business. We will be attending the Lakeview Dwelling Guild Expo Fair in October and are looking to finalize our booth design and get it ordered by 8/15. The booth layout is selected, and we have a logo and basic brand board. We are looking for graphic design that we can use for the next 3+ years without appearing dated. We are considering incorporating more of the baby blue color into our repaint branding (see bh-logo-dark blued-bg attached). The blue and white logo is our standard.
BrindleHold website: www.coatbrindle.example
Trade Show booth website: https://fernstandexhibits.example/10X10-Custom-Trade-Show-Display-Booth-I

```html
<!DOCTYPE html>
<html lang="en">
<head>
<meta charset="utf-8">
<title>Brindle Holdings, Inc. – Booth Graphics</title>
<link href="https://fonts.googleapis.com/css2?family=Raleway:wght@400;600&display=swap" rel="stylesheet">
<style>
  :root {
    --page-bg: #eceeed;
    --navy: #271768;
    --ink: #2a1a6b;
    --lavender: #cfd3ee;
    --pale-blue: #b9def4;
    --brand-light: #d4d6f0;
    --shelf: #f1f1f4;
    --screen: #2a2929;
  }
  * { margin: 0; padding: 0; box-sizing: border-box; }
  html, body { width: 804px; height: 1200px; overflow: hidden; background: var(--page-bg); }
  body { position: relative; font-family: "Raleway", sans-serif; }

  .backwall {
    position: absolute; left: 17px; top: 291px; width: 769px; height: 591px;
    background: var(--lavender);
    border-radius: 0 24px 0 0;
    overflow: hidden;
  }
  .backwall-artwork {
    position: absolute; inset: 0;
    background:
      radial-gradient(ellipse 60% 90% at 95% 55%, rgba(238,242,250,0.9), rgba(238,242,250,0) 70%),
      radial-gradient(ellipse 35% 80% at 52% 70%, rgba(244,120,170,0.45), rgba(244,120,170,0) 70%),
      radial-gradient(ellipse 30% 70% at 48% 80%, rgba(250,210,80,0.45), rgba(250,210,80,0) 70%),
      radial-gradient(ellipse 45% 80% at 62% 40%, var(--pale-blue), rgba(185,222,244,0) 75%),
      linear-gradient(135deg, var(--lavender), #dfe3f4);
  }
  .backwall-copy {
    position: absolute; left: 372px; width: 352px; top: 64px;
    text-align: center; color: var(--ink);
  }
  .headline { font-weight: 400; font-size: 25px; line-height: 29px; }
  .headline-rule { height: 1.5px; background: var(--ink); margin: 12px 8px 10px; }
  .markets { list-style: none; font-weight: 400; font-size: 25px; line-height: 30px; }

  .tower { position: absolute; left: 28px; top: 181px; width: 332px; height: 837px; }
  .tower-shape { position: absolute; inset: 0; }
  .tower-brand {
    position: absolute; left: 0; right: 0; top: 100px;
    text-align: center; color: var(--brand-light);
  }
  .brand-name { font-weight: 600; font-size: 16px; letter-spacing: 0.3px; }
  .brand-since { font-weight: 600; font-size: 10px; margin-top: 4px; }
  .tower-screen {
    position: absolute; left: 69px; top: 212px; width: 200px; height: 119px;
    background: var(--screen);
  }
  .tower-shelf {
    position: absolute; left: 58px; width: 217px; height: 7px; background: var(--shelf);
  }
  .shelf-upper { top: 388px; }
  .shelf-lower { top: 487px; }
</style>
</head>
<body>
  <section class="backwall">
    <div class="backwall-artwork" role="img" aria-label="Abstract swirl of rainbow and sky-blue ribbons over lavender"></div>
    <div class="backwall-copy">
      <h1 class="headline">Quality Painting Within<br>Texas &amp; Beyond Since 1972</h1>
      <div class="headline-rule"></div>
      <ul class="markets">
        <li>Garden</li>
        <li>High Rise</li>
        <li>Education</li>
        <li>Hospitality</li>
        <li>Office/Retail</li>
        <li>Senior Living</li>
        <li>Student Housing</li>
        <li>Urban Infill/Wrap/Mixed Use</li>
      </ul>
    </div>
  </section>

  <section class="tower">
    <svg class="tower-shape" viewBox="0 0 332 837" width="332" height="837" aria-hidden="true">
      <path fill="var(--navy)" d="M166,0 C260,0 316,45 330,75 C336,100 328,125 312,150 C285,185 278,210 278,230 L278,802 Q278,837 243,837 L89,837 Q54,837 54,802 L54,230 C54,210 47,185 20,150 C4,125 -4,100 2,75 C16,45 72,0 166,0 Z"/>
    </svg>
    <div class="tower-brand">
      <div class="brand-name">BRINDLE HOLDINGS, INC.</div>
      <div class="brand-since">Since 1972</div>
    </div>
    <div class="tower-screen"></div>
    <div class="tower-shelf shelf-upper"></div>
    <div class="tower-shelf shelf-lower"></div>
  </section>
</body>
</html>
```